LoomPages app needs an improved design

LoomPages makes available books that have been banned in certain countries. The current version of the app is available for download here: https://apps.quillmarket.example/details?id=org.tallbrook.loompage

At the moment, the app is available only in Chinese. Books are made available within the app, in text or audio format. Books can be downloaded for offline use. We created the app as a way to circumvent the intense censorship that is placed on book distribution inside China. The app is designed in such a way that the authorities are not able to censor the app, thus users in China are able to download the app, read content and receive updates to the app. So far over 100,000 people have used the app. Books are made available to the users for free and the app is also free to download.

We have used a similar anti-censorship strategy in a number of other apps, all with equally successful outcomes.

The app is only available on Android. While many Chinese purchase high end Android devices, Android is also the operating system of choice for new internet users in China. Oftentimes, the first time a user accesses the internet will be through an inexpensive Android smartphone.

This is very much a content driven app, with limited functionality but very visual. We need to optimize the app so that it is suitable for reading long texts. While we make available banned books through the app itself, our users are primarily avid readers - they are not likely to be netizens who wanted to download a book app just because it contains banned books. They will be readers who are interested in reading and exploring new books that are not normally available to them.

The app should have similar functionality to an e-reader, like a Vessly, however it needs to be optimized for smaller screens. Apps like Tornwick present content in an easy to read format.

Target Market(s)

Our current end users are Chinese who are professionals and have an interest in reading. They are likely between the ages of 18-50. We try to make the app as easy and intuitive as possible. Even though there are over 700 million people online in China, another 600 million of them will come online soon. We want experienced internet and technology users to easily find the content they are looking for and we want new internet and technology users to be able to easily use the app. Our users mainly use the app in the comfort of their own home - as they would read an e-book (Vessly) or in a quiet cafe.

Industry/Entity Type

Book Publisher

Font styles to use
Serif

Colors

Designer to choose colors to be used in the design.

Requirements
Must have
• Our current challenges include:
• - We want to promote new books as well as popular books (and potentially other categories) and allow users to browse more books in that category.
• - Allow users to search.
• - For each book, we need an indication whether it is an audio book or a text book.
• - For each book, we need an indication whether the book has already been downloaded.
• Our current audio book challenges include:
• - Show book cover.
• - Include all standard audio playback functions (pause, play, next chapter etc).
• - Audio books can play in the background. When the user leaves this view, the app needs to indicate that an audio book is playing in the background, and show the user how to return to this interface (to pause playback, etc).
• Our current text book challenges include:
• - Show name of book.
• - Maximize use of screen (since it may be hard to read on a small device).
• - Allow user to easily navigate (next page, any page number etc).

```html
<!DOCTYPE html>
<html lang="zh">
<head>
<meta charset="utf-8">
<title>Audiobook screens</title>
<link href="https://fonts.googleapis.com/css2?family=Noto+Sans+SC:wght@400;500;700&family=Roboto:wght@400;500&display=swap" rel="stylesheet">
<style>
:root{
  --bg:#b3daf2;
  --bar:#0e9ee0;
  --accent:#1a9be0;
  --ink:#222;
  --muted:#9a9a9a;
  --line:#c4c4c4;
  --nav:#8a8a8a;
  --cover:#4e5a4c;
  --cover-red:#c8242a;
  --white:#fff;
}
*{box-sizing:border-box;margin:0;padding:0}
html,body{width:1200px;height:806px;overflow:hidden;background:var(--bg)}
body{position:relative;font-family:"Noto Sans SC","Roboto",sans-serif;color:var(--ink)}
.section-title{position:absolute;left:26px;top:110px;font-family:"Roboto",sans-serif;font-weight:400;font-size:22px;color:#111}
.screen{position:absolute;top:160px;width:274px;height:486px;background:var(--white);overflow:hidden}
.s0{left:26px}.s1{left:316px}.s2{left:610px}.s3{left:902px}
.status{height:18px;background:var(--bar);color:var(--white);font:500 10px "Roboto",sans-serif;display:flex;justify-content:flex-end;align-items:center;gap:4px;padding-right:12px}
.status svg{display:block}
.icon{position:absolute}
.book-name{position:absolute;left:14px;top:66px;font-size:15px}
.book-meta{position:absolute;left:14px;top:90px;font:10px "Roboto","Noto Sans SC",sans-serif;color:var(--muted)}
.book-meta b{font-weight:500}
.cover-band{position:absolute;left:13px;top:114px;width:248px;height:110px;background:radial-gradient(ellipse at 50% 50%,#5f6b5c 0%,var(--cover) 70%)}
.chapters{position:absolute;left:13px;top:242px;width:248px;list-style:none}
.chapters li{height:31.6px;display:flex;align-items:center;font-size:10px}
.chapters .no{color:var(--muted);width:14px;font-family:"Roboto",sans-serif;font-size:9px}
.chapters .ttl{flex:1}
.chapters .dur{font-family:"Roboto",sans-serif;font-size:10px;width:40px;text-align:right}
.chapters .faded{opacity:.3}
.play-dot{width:20px;height:20px;border-radius:50%;background:var(--accent);margin-left:auto;margin-right:4px;display:flex;align-items:center;justify-content:center}
.fade{position:absolute;left:0;right:0;top:420px;height:30px;background:linear-gradient(rgba(255,255,255,0),#fff)}
.bottom-nav{position:absolute;left:0;right:0;top:448px;height:38px;display:flex;justify-content:space-around;align-items:center;background:var(--white)}
.player-title{position:absolute;left:0;right:0;top:64px;text-align:center;color:var(--accent);font-size:12px}
.cover{position:absolute}
.cover-main{left:86px;top:100px;width:100px;height:146px;background:linear-gradient(#56614f,var(--cover));box-shadow:0 1px 4px rgba(0,0,0,.35)}
.cover-left{left:0;top:114px;width:64px;height:116px;background:linear-gradient(#d23a2e,#9d1b1d)}
.cover-right{left:208px;top:114px;width:66px;height:116px;background:linear-gradient(90deg,#b3202a 20%,#5d4a48 60%,#8a6b5c)}
.p-name{position:absolute;left:0;right:0;top:256px;text-align:center;font-size:14px}
.p-author{position:absolute;left:0;right:0;top:278px;text-align:center;font-size:10px;color:var(--muted)}
.tabs{position:absolute;left:0;right:0;top:300px;text-align:center;font-size:10px;color:var(--muted)}
.tabs .on{color:var(--ink);font-weight:500}
.tabs .sep{margin:0 8px}
.controls{position:absolute;left:0;right:0;top:336px;display:flex;justify-content:center;align-items:center;gap:34px}
.big-play{width:44px;height:44px;border-radius:50%;background:var(--accent);display:flex;align-items:center;justify-content:center}
.times{position:absolute;left:13px;right:13px;top:388px;display:flex;justify-content:space-between;font:8px "Roboto",sans-serif}
.progress{position:absolute;left:13px;right:13px;top:406px;height:3px;background:#bbb}
.progress i{position:absolute;left:0;top:0;height:3px;width:29%;background:var(--accent)}
.progress b{position:absolute;left:29%;top:-4px;width:11px;height:11px;margin-left:-5px;border-radius:50%;background:#fff;border:1px solid #aaa}
.info-text{position:absolute;left:14px;right:14px;top:330px;font-size:8.6px;line-height:11.4px;color:#555;text-align:justify}
.info-text p{margin-bottom:10px}
.mini-player{position:absolute;left:0;right:0;top:446px;height:40px;background:var(--white);box-shadow:0 -1px 3px rgba(0,0,0,.12);display:flex;align-items:center;padding-left:12px}
.mini-cover{width:22px;height:30px;background:var(--cover)}
.mini-text{margin-left:10px;font-size:7.5px;line-height:11px;color:var(--accent);width:110px}
.mini-text .t{color:var(--ink)}
.mini-ctrl{margin-left:auto;margin-right:10px;display:flex;gap:18px;align-items:center}
.caption{position:absolute;top:668px;font-family:"Roboto",sans-serif;font-size:21px;color:#111;line-height:24px}
.c0{left:24px}.c1{left:316px}.c2{left:610px}.c3{left:902px}
.c0 span{display:block;padding-left:30px}
</style>
</head>
<body>
<svg width="0" height="0" style="position:absolute">
  <defs>
    <symbol id="i-status" viewBox="0 0 40 10">
      <path d="M0 9 L8 1 V9Z" fill="#fff"/>
      <path d="M12 3 A8 8 0 0 1 24 3 L18 9Z" fill="#fff"/>
      <rect x="29" y="1" width="4" height="8" fill="#fff"/>
    </symbol>
    <symbol id="i-back" viewBox="0 0 16 16"><path d="M15 8H2M8 2L2 8l6 6" fill="none" stroke="#1a9be0" stroke-width="1.8"/></symbol>
    <symbol id="i-close" viewBox="0 0 16 16"><path d="M2 2L14 14M14 2L2 14" fill="none" stroke="#1a9be0" stroke-width="1.8"/></symbol>
    <symbol id="i-more" viewBox="0 0 6 18"><circle cx="3" cy="2" r="1.8" fill="#1a9be0"/><circle cx="3" cy="9" r="1.8" fill="#1a9be0"/><circle cx="3" cy="16" r="1.8" fill="#1a9be0"/></symbol>
    <symbol id="i-queue" viewBox="0 0 20 16"><path d="M0 2h14M0 6h14M0 10h9" stroke="#1a9be0" stroke-width="2"/><path d="M16 1v10" stroke="#1a9be0" stroke-width="2"/><circle cx="14" cy="12" r="3" fill="#1a9be0"/></symbol>
    <symbol id="i-home" viewBox="0 0 16 16"><path d="M8 1L1 8h2v7h4v-4h2v4h4V8h2Z" fill="#8a8a8a"/></symbol>
    <symbol id="i-down" viewBox="0 0 16 16"><path d="M6 1h4v6h3l-5 5-5-5h3Z M2 14h12v2H2Z" fill="#1a9be0"/></symbol>
    <symbol id="i-search" viewBox="0 0 16 16"><circle cx="6.5" cy="6.5" r="4.8" fill="none" stroke="#8a8a8a" stroke-width="2"/><path d="M10 10l5 5" stroke="#8a8a8a" stroke-width="2.2"/></symbol>
    <symbol id="i-vmore" viewBox="0 0 6 18"><circle cx="3" cy="2" r="1.8" fill="#8a8a8a"/><circle cx="3" cy="9" r="1.8" fill="#8a8a8a"/><circle cx="3" cy="16" r="1.8" fill="#8a8a8a"/></symbol>
    <symbol id="i-prev" viewBox="0 0 16 16"><rect x="1" y="1" width="3" height="14" fill="#1a9be0"/><path d="M15 1v14L5 8Z" fill="#1a9be0"/></symbol>
    <symbol id="i-next" viewBox="0 0 16 16"><rect x="12" y="1" width="3" height="14" fill="#1a9be0"/><path d="M1 1v14L11 8Z" fill="#1a9be0"/></symbol>
    <symbol id="i-pause" viewBox="0 0 10 12"><rect x="0" y="0" width="3.4" height="12" fill="#fff"/><rect x="6.6" y="0" width="3.4" height="12" fill="#fff"/></symbol>
    <symbol id="i-play" viewBox="0 0 10 12"><path d="M1 0v12l9-6Z" fill="#fff"/></symbol>
  </defs>
</svg>

<h1 class="section-title">Audiobook</h1>

<section class="screen s0">
  <div class="status"><svg width="30" height="10"><use href="#i-status"/></svg>09:00</div>
  <svg class="icon" style="left:14px;top:31px" width="16" height="16"><use href="#i-back"/></svg>
  <svg class="icon" style="left:253px;top:30px" width="6" height="18"><use href="#i-more"/></svg>
  <div class="book-name">林海遠</div>
  <div class="book-meta">陳若禾 | <b>01 : 12 : 30</b></div>
  <div class="play-dot" style="position:absolute;left:248px;top:67px;width:19px;height:19px"><svg width="7" height="9"><use href="#i-play"/></svg></div>
  <div class="cover-band" role="img" aria-label="Blurred book cover with the cover in the centre"></div>
  <ul class="chapters">
    <li><span class="no">1.</span><span class="ttl">《林海远：鲜为人知的故事》, 选读（一）</span><span class="dur">25 : 16</span></li>
    <li><span class="no">2.</span><span class="ttl">《林海远：鲜为人知的故事》, 选读（二）</span><span class="dur">23 : 00</span></li>
    <li><span class="no">3.</span><span class="ttl">《林海远：鲜为人知的故事》, 选读（三）</span><span class="dur">12 : 12</span></li>
    <li><span class="no">4.</span><span class="ttl">《林海远：鲜为人知的故事》, 选读（四）</span><span class="dur">30 : 34</span></li>
    <li><span class="no">5.</span><span class="ttl">《林海远：鲜为人知的故事》, 选读（五）</span><span class="dur">26 : 03</span></li>
    <li><span class="no">6.</span><span class="ttl">《林海远：鲜为人知的故事》, 选读（六）</span><span class="dur">15 : 36</span></li>
    <li class="faded"><span class="no">7.</span><span class="ttl">《林海远：鲜为人知的故事》, 选读（七）</span><span class="dur">25 : 16</span></li>
  </ul>
  <div class="fade"></div>
  <nav class="bottom-nav">
    <svg width="16" height="16"><use href="#i-home"/></svg>
    <svg width="16" height="16"><use href="#i-down"/></svg>
    <svg width="16" height="16"><use href="#i-search"/></svg>
    <svg width="6" height="18"><use href="#i-vmore"/></svg>
  </nav>
</section>

<section class="screen s1">
  <div class="status"><svg width="30" height="10"><use href="#i-status"/></svg>09:00</div>
  <svg class="icon" style="left:14px;top:31px" width="16" height="16"><use href="#i-back"/></svg>
  <svg class="icon" style="left:241px;top:31px" width="20" height="16"><use href="#i-queue"/></svg>
  <div class="player-title">《林海远：鲜为人知的故事》, 选读（一）</div>
  <div class="cover cover-left" role="img" aria-label="Red cover of the previous book"></div>
  <div class="cover cover-main" role="img" aria-label="Current book cover with a portrait"></div>
  <div class="cover cover-right" role="img" aria-label="Red cover of the next book with a group photo"></div>
  <div class="p-name">林海遠</div>
  <div class="p-author">陳若禾</div>
  <div class="tabs"><span class="on">音频播放器</span><span class="sep">/</span><span>图书信息</span></div>
  <div class="controls">
    <svg width="18" height="18"><use href="#i-prev"/></svg>
    <div class="big-play"><svg width="17" height="20"><use href="#i-pause"/></svg></div>
    <svg width="18" height="18"><use href="#i-next"/></svg>
  </div>
  <div class="times"><span>14 : 32</span><span>25 : 16</span></div>
  <div class="progress"><i></i><b></b></div>
  <nav class="bottom-nav">
    <svg width="16" height="16"><use href="#i-home"/></svg>
    <svg width="16" height="16"><use href="#i-down"/></svg>
    <svg width="16" height="16"><use href="#i-search"/></svg>
    <svg width="6" height="18"><use href="#i-vmore"/></svg>
  </nav>
</section>

<section class="screen s2">
  <div class="status"><svg width="30" height="10"><use href="#i-status"/></svg>09:00</div>
  <svg class="icon" style="left:14px;top:31px" width="16" height="16"><use href="#i-back"/></svg>
  <svg class="icon" style="left:241px;top:31px" width="20" height="16"><use href="#i-queue"/></svg>
  <div class="player-title">《林海远：鲜为人知的故事》, 选读（一）</div>
  <div class="cover cover-left" role="img" aria-label="Red cover of the previous book"></div>
  <div class="cover cover-main" role="img" aria-label="Current book cover with a portrait"></div>
  <div class="cover cover-right" role="img" aria-label="Red cover of the next book with a group photo"></div>
  <div class="p-name">林海遠</div>
  <div class="p-author">陳若禾</div>
  <div class="tabs"><span>音频播放器</span><span class="sep">/</span><span class="on">图书信息</span></div>
  <div class="info-text">
    <p>还在台上风光得意时，周明远一度曾认真地想为江州的“打黑”修史、立传，当然作为公安局长，他的伟岸形象自然也会在其中昇华。他还特意叮嘱，不要把被他拿下的前江州司法局长唐立诚写的一无是处，要客观和公正，因为“只有事实才具有说服力”。但一年半后，随着他出逃美领馆，一切都改变了，彻底地改变了。</p>
    <p>虽然撰写江州“打黑”一书的素材如质变一般更加丰富，情节也更具有超越好莱坞电影的戏剧效果，但这部钱志恒“钦定”、周明远授意的书注定“难产”了，而且是以一种最有</p>
  </div>
  <div class="fade"></div>
  <nav class="bottom-nav">
    <svg width="16" height="16"><use href="#i-home"/></svg>
    <svg width="16" height="16"><use href="#i-down"/></svg>
    <svg width="16" height="16"><use href="#i-search"/></svg>
    <svg width="6" height="18"><use href="#i-vmore"/></svg>
  </nav>
</section>

<section class="screen s3">
  <div class="status"><svg width="30" height="10"><use href="#i-status"/></svg>09:00</div>
  <svg class="icon" style="left:14px;top:31px" width="14" height="14"><use href="#i-close"/></svg>
  <svg class="icon" style="left:258px;top:30px" width="6" height="18"><use href="#i-more"/></svg>
  <div class="book-name">林海遠</div>
  <div class="book-meta">陳若禾 | <b>01 : 12 : 30</b></div>
  <div class="cover-band" role="img" aria-label="Blurred book cover with the cover in the centre"></div>
  <ul class="chapters">
    <li><span class="no">1.</span><span class="ttl">《林海远：鲜为人知的故事》, 选读（一）</span><span class="play-dot"><svg width="8" height="9"><use href="#i-pause"/></svg></span></li>
    <li><span class="no">2.</span><span class="ttl">《林海远：鲜为人知的故事》, 选读（二）</span><span class="dur">23 : 00</span></li>
    <li><span class="no">3.</span><span class="ttl">《林海远：鲜为人知的故事》, 选读（三）</span><span class="dur">12 : 12</span></li>
    <li><span class="no">4.</span><span class="ttl">《林海远：鲜为人知的故事》, 选读（四）</span><span class="dur">30 : 34</span></li>
    <li><span class="no">5.</span><span class="ttl">《林海远：鲜为人知的故事》, 选读（五）</span><span class="dur">26 : 03</span></li>
    <li><span class="no">6.</span><span class="ttl">《林海远：鲜为人知的故事》, 选读（六）</span><span class="dur">15 : 36</span></li>
    <li class="faded"><span class="no">7.</span><span class="ttl">《林海远：鲜为人知的故事》, 选读（七）</span><span class="dur">25 : 16</span></li>
  </ul>
  <div class="mini-player">
    <div class="mini-cover" role="img" aria-label="Small book cover thumbnail"></div>
    <div class="mini-text">林海远：鲜为人知的故事》,<br>选读（一）| <span class="t">25 : 16</span></div>
    <div class="mini-ctrl">
      <svg width="12" height="12"><use href="#i-prev"/></svg>
      <div class="play-dot" style="margin:0"><svg width="8" height="9"><use href="#i-pause"/></svg></div>
      <svg width="12" height="12"><use href="#i-next"/></svg>
    </div>
  </div>
</section>

<div class="caption c0">4.0 Audiobook page after<span>download</span></div>
<div class="caption c1">4.1 Audiobook player</div>
<div class="caption c2">4.2 Audiobook Information</div>
<div class="caption c3">4.3&nbsp; View playlist or chapter</div>
</body>
</html>
```